Flyer for American Indian Elders on Dementia Warning Signs

We need a flyer designed for older adults who are American Indian or Alaska Native (in the U.S.).

Ideally, the flyer should complement the colors of our logos. The project logo and our organization logo are attached to the brief.

When people see the flyer we want them to feel that it represents their culture, is warm, and professional but relatable to older adults and people who have limited incomes.

I have attached an earlier draft of the document we designed ourselves BUT we want different and better.

It is for older adults who have trouble reading so:
1. you must use a font that is 11.5 points or larger
2. Do not put text over complex pictures or use shading with words
3. You can use a serif font for the heading, but should use san serif for the body text
4. There should be good contrast between the font color and background

Please do not use any images that include a head dress or pictures of American Indian people or things that are very traditional or "token" imagery.

We need to save a small space under the call out box/ somewhere on the flyer for other people to add their logo once they download.

Let us know if you have questions or need additional information.

Target Market(s)

Older American Indian people

Font styles to use
Serif
Sans Serif

Requirements
Must have
• Easy to read for older adults
Should not have
• indian headdress

```html
<!DOCTYPE html>
<html lang="en">
<head>
<meta charset="utf-8">
<title>10 Signs of Thinking or Memory Changes that Might be Dementia</title>
<link rel="stylesheet" href="https://fonts.googleapis.com/css2?family=Montserrat:wght@400;500;600;700&display=swap">
<style>
  :root {
    --ink-black: #121212;
    --ink-white: #ffffff;
    --ink-dark: #1d2b33;
    --accent-red: #e8452e;
    --callout-red: #d4503f;
    --panel-grey: #efefef;
    --teal-top: #2cbfc2;
    --teal-mid: #2ca1b4;
    --teal-bottom: #2c6f92;
    --photo-dark: #1c1512;
    --photo-skin: #8a5a3e;
  }
  * { box-sizing: border-box; margin: 0; padding: 0; }
  html, body { width: 900px; height: 1200px; overflow: hidden; }
  body {
    font-family: "Montserrat", Arial, sans-serif;
    background: var(--panel-grey);
  }
  .flyer {
    position: relative;
    width: 900px;
    height: 1200px;
    overflow: hidden;
    background: linear-gradient(180deg, var(--teal-top) 375px, var(--teal-mid) 760px, var(--teal-bottom) 1200px);
  }
  .header-band {
    position: absolute;
    left: 0; top: 0;
    width: 900px; height: 375px;
    background: var(--ink-black);
  }
  .header-photo {
    position: absolute;
    right: 0; top: 0;
    width: 380px; height: 330px;
    background:
      radial-gradient(ellipse 140px 190px at 55% 45%, var(--photo-skin) 0%, rgba(138,90,62,0.35) 55%, transparent 80%),
      linear-gradient(135deg, var(--ink-black) 0%, var(--photo-dark) 60%, #3a2a22 100%);
  }
  .title {
    position: absolute;
    left: 27px; top: 30px;
    width: 500px;
    font-size: 29px;
    font-weight: 500;
    line-height: 1.2;
    color: var(--ink-white);
  }
  .title .title-accent {
    display: block;
    color: var(--accent-red);
    font-weight: 700;
  }
  .intro {
    position: absolute;
    left: 27px; top: 166px;
    width: 680px;
    font-size: 17px;
    line-height: 1.3;
    color: var(--ink-white);
  }
  .intro p + p { margin-top: 22px; }

  .signs {
    position: absolute;
    left: 30px; top: 393px;
    width: 846px;
    list-style: none;
    counter-reset: sign;
  }
  .signs li {
    position: relative;
    counter-increment: sign;
    padding-left: 30px;
    font-size: 16.6px;
    line-height: 1.3;
    color: var(--ink-dark);
    margin-bottom: 17px;
    width: 505px;
  }
  .signs li.wide { width: 846px; }
  .signs li::before {
    content: counter(sign) ".";
    position: absolute;
    left: 0; top: 0;
    width: 24px;
    text-align: right;
    font-weight: 600;
  }
  .signs li:nth-child(10)::before { left: -8px; width: 32px; }
  .signs strong { font-weight: 600; }

  .points-panel {
    position: absolute;
    left: 551px; top: 328px;
    width: 349px; height: 683px;
    background: var(--panel-grey);
    border-radius: 56px 0 0 48px;
    padding: 60px 24px 0 22px;
  }
  .points-title {
    font-size: 28px;
    font-weight: 700;
    color: var(--accent-red);
    margin-left: -3px;
  }
  .points-list {
    list-style: none;
    margin-top: 14px;
  }
  .points-list li {
    position: relative;
    padding-left: 19px;
    font-size: 16.6px;
    line-height: 1.28;
    color: var(--ink-dark);
    margin-bottom: 21px;
  }
  .points-list li::before {
    content: "";
    position: absolute;
    left: 0; top: 8px;
    width: 7px; height: 7px;
    border-radius: 50%;
    background: var(--accent-red);
  }
  .learn-more {
    position: absolute;
    left: 533px; top: 803px;
    width: 325px; height: 122px;
    background: var(--callout-red);
    color: var(--ink-white);
    font-size: 13px;
    line-height: 1.3;
    padding: 12px 20px 0 48px;
  }
  .learn-more .links { margin-top: 16px; font-style: italic; }
  .partner-row {
    position: absolute;
    left: 577px; top: 950px;
    width: 310px;
    display: flex;
    align-items: center;
    justify-content: space-between;
  }
  .partner {
    display: flex;
    align-items: center;
    gap: 6px;
    font-size: 10px;
    font-weight: 600;
    line-height: 1.15;
    color: var(--accent-red);
    text-transform: uppercase;
  }
  .partner .mark {
    width: 28px; height: 28px;
    border-radius: 50%;
    background: var(--teal-mid);
    flex: none;
  }
  .partner .mark.square { border-radius: 0; width: 22px; height: 22px; }
</style>
</head>
<body>
<main class="flyer">
  <section class="header-band">
    <div class="header-photo" role="img" aria-label="Photo of an elder's hand holding a child's hand against a dark background"></div>
    <h1 class="title">10 Signs of Thinking<br>or Memory Changes that <span class="title-accent">Might be Dementia</span></h1>
    <div class="intro">
      <p>As we get older, we may slow down a bit. This is a normal<br>part of aging. Changes in memory or thinking that make it<br>harder to get through the day, are not a normal part of aging.<br>These may be early signs of dementia.</p>
      <p>Because American Indian and Alaska Native people have a high risk<br>of dementia, it is important to know the warning signs. Do you have<br>any of these 10 signs? If so, talk to your doctor.</p>
    </div>
  </section>

  <ol class="signs">
    <li><strong>Memory loss that affects your daily life.</strong> You may forget events or important dates; repeat yourself; rely more often on lists or sticky notes to remember things more often</li>
    <li><strong>Trouble planning or solving problems.</strong> You may have a harder time paying bills; cooking recipes you have used for years</li>
    <li><strong>Get onfused about the time, date, or where you are.</strong></li>
    <li><strong>Daily tasks are getting harder, including</strong> driving; making a grocery list or going shopping</li>
    <li><strong>Trouble with how your eyesight and thinking work together that gets worse.</strong> This includes tripping, falls, or problems with your balance; spilling or dropping things more</li>
    <li><strong>New trouble talking or writing.</strong> You have a hard time finding the words you want to say. For example, you may say “that thing on your wrist that tells time” instead of “watch.”</li>
    <li><strong>Lose and cannot find things.</strong> For example, you can’t find the coffee pot that you use every day; might put your car keys in the freezer</li>
    <li><strong>Notice changes in your mood or personality</strong>, such as being easily mad or sad in everyday situations; more fearful (scared) or suspicious (not trusting)</li>
    <li class="wide"><strong>Act different and make poor choices.</strong>This may make you more likely to spend money you do not have or be a scam victim; stop washing up regularly or pay less attention to how you look; forget to take care of your pet</li>
    <li class="wide"><strong>Pull away from friends and family because it is harder to keep up.</strong> You may not want to do things you used to enjoy, like sporting events, church, music, or sex.</li>
  </ol>

  <aside class="points-panel">
    <h2 class="points-title">Main Points</h2>
    <ul class="points-list">
      <li>American Indian and Alaska Native people have a higher risk of dementia.</li>
      <li>Big changes in memory or thinking that make it hard to get through the day are not a normal part of aging.</li>
      <li>People with one or more of these 10 signs should talk to their doctor to find the cause. It is not always dementia.</li>
      <li>Early dementia diagnosis gives you a chance to get care and plan your future.</li>
    </ul>
  </aside>

  <div class="learn-more">
    <p>To learn more about the warning signs of dementia in American Indian and Alaska Native people, visit:</p>
    <p class="links">www.eldermindwellness.org<br>www.healthyagingguide.org</p>
  </div>

  <div class="partner-row">
    <div class="partner"><span class="mark"></span><span>Elder Mind<br>Wellness Center</span></div>
    <div class="partner"><span class="mark square"></span><span>Circle of Aging<br>Network</span></div>
  </div>
</main>
</body>
</html>
```